Professional Website for Commercial Real Estate Broker

I own a small boutique commercial real estate company called Harbinridge Realty.
My current website is www.movewithquorl.com and is hosted on hostelmira. I am looking for an all new website that will allow me to compete with bigger players in our industry. In other words, I need something professional, sleek, and functional.

I am looking for a designer that can take my complete website all the way to coding, migration, and launch. I understand that this may be an add'l charge, so please include with your design submission what the add'l charge will be to take the website to launch with all functionality as described below.

As an example of a page in my industry that I like please check out: www.tobiaskellner.com.

My logo is attached and my main colors are the blue, white, grey - similar to the logo.

I am looking for a five page website with the following pages:

Home
Harbinridge Team
Services
Sold Properties
Contact

A couple of features that I will want on the site are:

- I want to make sure that we can imbed a news commercial real estate news feed from: http://www.bizplotwire.com/news/ on the website's home page, similar to how it is on tobiaskellner.com.

- Sold Properties page will allow me to upload the following information on to the website so that I can add new properties that I have recently sold on a weekly or monthly basis. I would like the information to be displayed similarly to http://www.tobiaskellner.com/properties.html . I should be able to upload: picture, price, bldg size, lot size, closing date for each property. This will require a user friendly back end that I can navigate.

- On the home page, I also want to have a form where visitors can request a Market Analysis of their property by entering: Name, property address, email address, phone number. I will be sent an email with this information and I can follow up via telephone or email direct.

- The Harbinridge Team page will have a picture, contact info, and brief bio for each member of the team. I would like to be able to adjust this on a user friendly back end.

I have included my Company Logo. Feel free to use any text from my current website: www.movewithquorl.com. Also, any sleek looking stock photos of office / commercial buildings can be used for the initial design purposes.

I look forward to getting your design submittal and moving forward asap!

Target Market(s)

Los Angeles real estate brokers, developers, and investors.

Industry/Entity Type

Real Estate

Coding

Coded - Design and coding required

Number of Pages Required

5+ page

Font styles to use
Sans Serif

Colors
ffffff
85abd2
0455a3
b2b2b2
000000
3276b5

Requirements
Must have
• Sleek and professional design.
• - I want to make sure that we can imbed a news commercial real estate news feed from: http://www.bizplotwire.com/news/ on the website's home page, similar to how it is on tobiaskellner.com.
• - Sold Properties page will allow me to upload the following information on to the website so that I can add new properties that I have recently sold on a weekly or monthly basis. I would like the information to be displayed similarly to http://www.tobiaskellner.com/properties.html . I should be able to upload: picture, price, bldg size, lot size, closing date for each property. This will require a user friendly back end that I can navigate.
• - On the home page, I also want to have a form where visitors can request a Market Analysis of their property by entering: Name, property address, email address, phone number. I will be sent an email with this information and I can follow up via telephone or email direct.
Nice to have
• Dynamic banner on the home page with beautiful photos that change every few seconds.

```html
<!DOCTYPE html>
<html lang="en">
<head>
<meta charset="utf-8">
<title>Harbinridge Realty</title>
<link rel="stylesheet" href="https://fonts.googleapis.com/css2?family=Poppins:wght@400;500;600&family=Open+Sans:ital,wght@0,400;0,600;1,400&display=swap">
<style>
:root{
  --blue:#0455a3;
  --blue-mid:#3276b5;
  --blue-light:#85abd2;
  --grey:#b2b2b2;
  --ink:#1a1a1a;
  --text:#555;
  --red:#ef2b2d;
  --topbar:#efefef;
  --footer:#232323;
  --newsletter:#2d2d2d;
  --bottom:#1b1b1b;
  --white:#fff;
}
*{box-sizing:border-box;margin:0;padding:0}
html,body{width:1200px;height:2655px;overflow:hidden}
body{font-family:"Open Sans",sans-serif;color:var(--text);background:var(--white);position:relative}
.abs{position:absolute}

/* top bar */
.topbar{position:absolute;top:0;left:0;width:1200px;height:36px;background:var(--topbar);font-size:13px;color:#444}
.topbar .links{position:absolute;left:66px;top:9px;display:flex;gap:20px;align-items:center}
.topbar .links span{display:flex;align-items:center;gap:6px}
.dot{width:12px;height:12px;background:var(--blue);display:inline-block;border-radius:2px}
.topbar .social{position:absolute;right:66px;top:8px;display:flex;gap:6px}
.topbar .social i{width:19px;height:19px;border-radius:50%;background:var(--blue);display:block}

/* header */
.header{position:absolute;top:36px;left:0;width:1200px;height:114px;background:var(--white)}
.brand{position:absolute;left:68px;top:40px;display:flex;align-items:center;gap:10px;font-family:"Poppins",sans-serif;font-weight:600;font-size:26px;color:var(--blue)}
.brand .sq{width:26px;height:26px;background:var(--grey)}
.contact-item{position:absolute;top:36px;display:flex;gap:16px;font-size:14px;color:#222;line-height:22px}
.contact-item b{font-weight:600;font-size:15px}

/* hero */
.hero{position:absolute;top:150px;left:0;width:1200px;height:546px;background:linear-gradient(180deg,#3b4350 0%,#4f5966 40%,#3a4c5c 70%,#2a3c4a 100%)}
.hero-title{position:absolute;left:116px;top:162px;font-family:"Poppins",sans-serif;font-weight:400;font-size:30px;color:var(--white);letter-spacing:.5px}
.field{position:absolute;top:227px;height:41px;background:#e9e9e9;border-radius:2px;font-size:14px;color:#999;padding:11px 14px}
.search-btn{position:absolute;left:1009px;top:227px;width:62px;height:41px;background:var(--blue);border-radius:2px}
.more{position:absolute;left:118px;top:302px;font-size:16px;color:var(--white);display:flex;align-items:center;gap:12px}
.more .adv{border:2px solid var(--white);padding:3px 10px;font-size:15px;border-radius:2px}
.count{position:absolute;left:120px;top:358px;font-family:"Poppins",sans-serif;font-size:28px;color:var(--white)}

/* nav */
.nav{position:absolute;top:696px;left:0;width:1200px;height:53px;background:var(--blue)}
.nav a{position:absolute;top:16px;font-family:"Poppins",sans-serif;font-size:16px;color:var(--white);text-decoration:none}
.nav .active::after{content:"";position:absolute;left:-8px;right:-8px;top:33px;height:4px;background:#111}

/* about */
.about-photo{position:absolute;left:67px;top:818px;width:356px;height:317px;background:linear-gradient(135deg,#e8e2d8,#c9b8a2 60%,#f1eee9)}
.about-logo{position:absolute;left:453px;top:818px;display:flex;align-items:center}
.about-logo .box{width:122px;height:85px;border:4px solid var(--blue);border-right:none}
.about-logo .name{font-family:"Poppins",sans-serif;font-size:26px;color:var(--blue);margin-left:-70px;background:var(--white);padding:0 4px}
.about-text{position:absolute;left:453px;top:912px;width:680px;font-size:14.5px;line-height:21px;color:#444}
.about-text p{margin-bottom:16px}
.features{position:absolute;left:453px;top:1080px;display:flex;gap:38px}
.feature{display:flex;gap:14px;width:205px}
.feature h4{font-family:"Poppins",sans-serif;font-size:13.5px;font-weight:500;color:#222}
.feature p{font-size:13px;line-height:19px;color:#333}

/* market analysis */
.cta{position:absolute;top:1218px;left:0;width:1200px;height:368px;background:linear-gradient(180deg,#1c58a4,#1a4f95 60%,#184a8d)}
.cta-rule{position:absolute;left:300px;width:600px;height:1px;background:rgba(255,255,255,.45)}
.cta h2{position:absolute;left:0;width:1200px;top:56px;text-align:center;font-family:"Poppins",sans-serif;font-weight:600;font-size:31px;color:var(--white)}
.cta p{position:absolute;left:120px;width:960px;top:124px;text-align:center;font-size:14.5px;line-height:22px;color:var(--white)}
.input{position:absolute;height:40px;background:var(--white);font-size:13px;color:#999;padding:12px}
.cta .go{position:absolute;left:491px;top:296px;width:198px;height:41px;background:var(--red);font-family:"Poppins",sans-serif;font-weight:600;font-size:17px;color:var(--white);text-align:center;line-height:41px}

/* news */
.news-title{position:absolute;left:65px;top:1640px;font-family:"Poppins",sans-serif;font-weight:500;font-size:25px;color:#111}
.news-rule{position:absolute;left:65px;top:1691px;width:1045px;height:1px;background:#ddd}
.card{position:absolute;top:1729px;width:328px}
.card .photo{height:178px}
.card .date{position:absolute;left:8px;top:130px;width:56px;height:56px;background:var(--red);color:var(--white);text-align:center;font-family:"Poppins",sans-serif;line-height:1}
.card .date b{display:block;font-size:20px;font-weight:600;padding-top:8px}
.card .date span{font-size:12px}
.card .bar{height:5px;background:var(--red);margin-top:3px}
.card .meta{margin-top:24px;font-size:13px;font-style:italic;color:#777}
.card h3{margin-top:12px;font-family:"Poppins",sans-serif;font-weight:600;font-size:17px;line-height:22px;color:#111}
.card p{margin-top:12px;font-size:14px;line-height:25px;color:#888}

/* footer */
.footer{position:absolute;top:2167px;left:0;width:1200px;height:279px;background:var(--footer)}
.footer-brand{position:absolute;left:0;width:1200px;top:70px;text-align:center;font-family:"Poppins",sans-serif;font-weight:600;font-size:28px;color:#ddd}
.footer p{position:absolute;left:300px;width:600px;top:134px;text-align:center;font-size:15px;line-height:24px;color:#ccc}
.footer .social{position:absolute;left:486px;top:207px;display:flex;gap:9px}
.footer .social i{width:30px;height:30px;border-radius:50%;background:var(--white);display:block}

.newsletter{position:absolute;top:2446px;left:0;width:1200px;height:142px;background:var(--newsletter)}
.newsletter .label{position:absolute;left:186px;top:46px;font-family:"Poppins",sans-serif;color:var(--white);line-height:1.05}
.newsletter .label small{font-size:18px;display:block}
.newsletter .label span{font-size:25px}
.newsletter .email{position:absolute;left:376px;top:80px;width:670px;border-bottom:1px solid #888;font-size:12px;color:#ddd;padding-bottom:6px}

.bottombar{position:absolute;top:2588px;left:0;width:1200px;height:67px;background:var(--bottom);font-size:13px;color:#ddd}
.bottombar .links{position:absolute;left:67px;top:24px}
.bottombar .links em{font-style:normal;margin:0 11px}
.bottombar .copy{position:absolute;right:66px;top:24px}
</style>
</head>
<body>

<div class="topbar">
  <div class="links">
    <span><i class="dot"></i>Submit Property</span>
    <span><i class="dot"></i>Login or Register</span>
    <span><i class="dot"></i>English ▾</span>
  </div>
  <div class="social"><i></i><i></i><i></i></div>
</div>

<header class="header">
  <div class="brand"><span class="sq"></span>Harbinridge Realty</div>
  <div class="contact-item" style="left:626px">
    <svg width="26" height="42" viewBox="0 0 26 42"><rect x="2" y="2" width="22" height="38" rx="3" fill="none" stroke="#0455a3" stroke-width="2"/><line x1="2" y1="8" x2="24" y2="8" stroke="#0455a3" stroke-width="2"/><line x1="2" y1="32" x2="24" y2="32" stroke="#0455a3" stroke-width="2"/></svg>
    <div><b>(424) 555-0147</b><br>hello@movewithquorl.com</div>
  </div>
  <div class="contact-item" style="left:846px">
    <svg width="30" height="44" viewBox="0 0 30 44"><path d="M15 2C8 2 3 7 3 14c0 10 12 26 12 26s12-16 12-26C27 7 22 2 15 2z" fill="none" stroke="#0455a3" stroke-width="2"/><circle cx="15" cy="14" r="4" fill="none" stroke="#0455a3" stroke-width="2"/></svg>
    <div><b>2250 Larkmere Blvd. Ste 310</b><br>Los Angeles, CA 90099</div>
  </div>
</header>

<section class="hero" role="img" aria-label="Dusk view of a luxury waterfront villa with pool and wooden deck">
  <h1 class="hero-title">FIND YOUR DREAM HOME</h1>
  <div class="field" style="left:115px;width:239px">Any type</div>
  <div class="field" style="left:379px;width:239px">Any Status</div>
  <div class="field" style="left:637px;width:356px">Enter address e.g. steet, city or state
    <svg class="abs" style="right:12px;top:12px" width="18" height="18" viewBox="0 0 18 18"><circle cx="9" cy="9" r="7" fill="none" stroke="#666" stroke-width="1.5"/><circle cx="9" cy="9" r="2.5" fill="#666"/></svg>
  </div>
  <div class="search-btn"><svg class="abs" style="left:22px;top:11px" width="19" height="19" viewBox="0 0 19 19"><circle cx="8" cy="8" r="6" fill="none" stroke="#fff" stroke-width="2.5"/><line x1="12.5" y1="12.5" x2="17.5" y2="17.5" stroke="#fff" stroke-width="2.5"/></svg></div>
  <div class="more">Need more search options? <span class="adv">Advanced Search</span></div>
  <div class="count">We have 10 properties for you!</div>
</section>

<nav class="nav">
  <a class="active" style="left:103px">HOME</a>
  <a style="left:236px">HARBINRIDGE TEAM</a>
  <a style="left:430px">SERVICES</a>
  <a style="left:582px">SOLD PROPERTIES</a>
  <a style="left:814px">CONTACT</a>
</nav>

<div class="about-photo" role="img" aria-label="Couple receiving house keys from an agent beside a sold sign"></div>
<div class="about-logo"><div class="box"></div><span class="name">Harbinridge Realty</span></div>
<div class="about-text">
  <p>Harbinridge Realty is a commercial real estate brokerage firm that provides a range of services to assist each of our clients in reaching their real estate objectives quickly and efficiently.</p>
  <p>Our focus on Southern California investment properties allows us to have a unique and focused perspective on this highly competitive market. Through our experience, diligence and resourcefulness, we help our clients make informed real estate decisions with their specific goals in mind.</p>
</div>
<div class="features">
  <div class="feature"><svg width="44" height="42" viewBox="0 0 44 42"><path d="M3 20L22 4l19 16" fill="none" stroke="#0455a3" stroke-width="2.5"/><rect x="9" y="18" width="26" height="20" fill="none" stroke="#0455a3" stroke-width="2.5"/><rect x="18" y="26" width="8" height="12" fill="#3276b5"/></svg><div><h4>HOMES FOR SALE</h4><p>We are Offering the Best Real Estate Services</p></div></div>
  <div class="feature"><svg width="44" height="42" viewBox="0 0 44 42"><path d="M3 20L22 4l19 16" fill="none" stroke="#0455a3" stroke-width="2.5"/><rect x="9" y="18" width="26" height="20" fill="none" stroke="#0455a3" stroke-width="2.5"/><rect x="18" y="26" width="8" height="12" fill="#3276b5"/></svg><div><h4>HOMES FOR SALE</h4><p>We are Offering the Best Real Estate Services</p></div></div>
  <div class="feature"><svg width="44" height="42" viewBox="0 0 44 42"><path d="M3 20L22 4l19 16" fill="none" stroke="#0455a3" stroke-width="2.5"/><rect x="9" y="18" width="26" height="20" fill="none" stroke="#0455a3" stroke-width="2.5"/><rect x="18" y="26" width="8" height="12" fill="#3276b5"/></svg><div><h4>HOMES FOR SALE</h4><p>We are Offering the Best Real Estate Services</p></div></div>
</div>

<section class="cta" aria-label="Request a market analysis">
  <div class="cta-rule" style="top:52px"></div>
  <h2>HARBINRIDGE REALTY SELLING FOR?</h2>
  <div class="cta-rule" style="top:110px"></div>
  <p>Curious what your property is worth? We advise Los Angeles owners, developers and investors on office, retail and multifamily assets. Request a free Market Analysis and we will follow up by phone or email.</p>
  <div class="input" style="left:255px;top:190px;width:216px">Your Name</div>
  <div class="input" style="left:483px;top:190px;width:216px">Email Address</div>
  <div class="input" style="left:711px;top:190px;width:216px">Phone Number</div>
  <div class="input" style="left:255px;top:240px;width:672px">Type Your Property Address.....</div>
  <div class="go">FIND OUT !</div>
</section>

<h2 class="news-title">COMMERCIAL REAL ESTATE NEWS</h2>
<div class="news-rule"></div>

<article class="card" style="left:65px">
  <div class="photo" role="img" aria-label="Modern dark timber house with glass facade and deck" style="background:linear-gradient(180deg,#8fb2d6,#5a4a3e 55%,#9a7a5c)"></div>
  <div class="date"><b>05</b><span>Aug</span></div><div class="bar"></div>
  <div class="meta">By: Lenna Corvath &nbsp;&nbsp;| Comments:6</div>
  <h3>Is Investing in Westside Office Space a good idea ?</h3>
  <p>Vacancy rates are easing across the Westside as owners adjust rents and tenants seek flexible terms.</p>
</article>
<article class="card" style="left:435px">
  <div class="photo" role="img" aria-label="Contemporary house courtyard with lounge chairs and trees" style="background:linear-gradient(180deg,#d8dcd8,#8a8f86 50%,#5d5348)"></div>
  <div class="date"><b>05</b><span>Aug</span></div><div class="bar"></div>
  <div class="meta">By: Lenna Corvath &nbsp;&nbsp;| Comments:6</div>
  <h3>Are Mid-City Retail Centers still a good idea ?</h3>
  <p>Neighborhood retail with grocery anchors continues to draw steady demand from private investors.</p>
</article>
<article class="card" style="left:805px">
  <div class="photo" role="img" aria-label="White modern villa with large windows and a pool" style="background:linear-gradient(180deg,#7fb3e6,#eef0f0 45%,#4a8fb8)"></div>
  <div class="date"><b>05</b><span>Aug</span></div><div class="bar"></div>
  <div class="meta">By: Lenna Corvath &nbsp;&nbsp;| Comments:6</div>
  <h3>Is Investing in Valley Multifamily a good idea ?</h3>
  <p>Cap rates hold firm for smaller apartment buildings as rental demand stays strong in the Valley.</p>
</article>

<footer class="footer">
  <div class="footer-brand">Harbinridge Realty</div>
  <p>Pellentesque habitant morbi tristique senetus et netus et malesuada fames ac turpis . tortor quam, feugiat vitae.</p>
  <div class="social"><i></i><i></i><i></i><i></i><i></i><i></i></div>
</footer>

<section class="newsletter">
  <svg class="abs" style="left:104px;top:46px" width="62" height="50" viewBox="0 0 62 50"><path d="M4 16L31 4l27 12v30H4z" fill="none" stroke="#fff" stroke-width="2.5"/><path d="M4 16l27 18 27-18" fill="none" stroke="#fff" stroke-width="2.5"/></svg>
  <div class="label"><small>OUR</small><span>NEWSLETTER</span></div>
  <div class="email">ENTER YOUR E-MAIL ADDRESS..</div>
  <svg class="abs" style="left:1006px;top:58px" width="30" height="28" viewBox="0 0 30 28"><path d="M2 14L28 2 22 26 14 18z" fill="#fff"/></svg>
</section>

<div class="bottombar">
  <div class="links">Home<em>|</em>Harbinridge Team<em>|</em>Services<em>|</em>Sold Properties<em>|</em>Contact</div>
  <div class="copy">Harbinridge Realty. Copyright © 2011-2017 Quorl Works, Inc.</div>
</div>

</body>
</html>
```